Stationery Design Project

We are a packaging machinery manufacturer that mainly serve the food industry.
We now require a full set of stationary including name card, envelop, letter paper, and etc. to match our company image. The logo has been awarded in a previous contest which is attached here.
Updates
Project Deadline Extended
Reason: We have extended the deadline. We have adjusted the deadline before launch to avoid confusion but it turns out the new date wasn't implemented by the system. All designers please feel free to submit your design. Thank you!
Target Market(s)
B2B customer, including decision maker in food factories, chemical factories, etc.
Industry/Entity Type
Industry
Colors
Designer to choose colors to be used in the design.
Look and feel
Each slider illustrates characteristics of the customer's brand and the style your logo design should communicate.

```html
<!DOCTYPE html>
<html lang="en">
<head>
<meta charset="UTF-8">
<title>Vorenta Stationery</title>
<link rel="stylesheet" href="https://fonts.googleapis.com/css2?family=Open+Sans:wght@400;600;700;800&display=swap">
<style>
  :root {
    --green: #036a3a;
    --grey: #8b9196;
    --text-grey: #7a7f84;
    --white: #ffffff;
    --backdrop: #e4e4e4;
  }
  * { margin: 0; padding: 0; box-sizing: border-box; }
  html, body { width: 1200px; height: 900px; overflow: hidden; }
  body {
    background: var(--backdrop);
    font-family: "Open Sans", Arial, sans-serif;
    position: relative;
  }
  .sheet { position: absolute; background: var(--white); overflow: hidden; }

  .brand { position: absolute; display: flex; flex-direction: column; }
  .brand-row { display: flex; align-items: center; gap: 4px; }
  .brand-mark { background: currentColor; display: block; flex: none; }
  .brand-name { font-weight: 800; line-height: 1; letter-spacing: 0.5px; white-space: nowrap; }
  .brand-tagline { font-weight: 700; letter-spacing: 1.6px; line-height: 1; white-space: nowrap; }

  /* business card front */
  .card-front { left: 118px; top: 205px; width: 400px; height: 230px; }
  .card-front .brand { left: 32px; top: 40px; color: var(--green); }
  .card-front .brand-mark { width: 18px; height: 18px; }
  .card-front .brand-name { font-size: 21px; }
  .card-front .brand-tagline { font-size: 6.5px; color: var(--text-grey); margin-top: 2px; }
  .name-band { position: absolute; left: 0; top: 93px; width: 400px; height: 54px; }
  .holder { position: absolute; left: 27px; top: 101px; color: var(--white); }
  .holder-name { font-size: 18px; font-weight: 400; line-height: 1.15; }
  .holder-role { font-size: 11px; line-height: 1.2; }
  .contact { position: absolute; left: 26px; font-size: 9.5px; color: var(--text-grey); line-height: 1.25; display: flex; align-items: center; gap: 3px; white-space: nowrap; }
  .contact svg { flex: none; }
  .web { position: absolute; font-weight: 700; color: var(--green); font-size: 10px; white-space: nowrap; }
  .card-front .web { right: 28px; top: 199px; }

  /* business card back */
  .card-back { left: 118px; top: 458px; width: 400px; height: 230px; background: var(--grey); }
  .card-back .brand { left: 102px; top: 98px; color: var(--white); }
  .card-back .brand-mark { width: 32px; height: 32px; }
  .card-back .brand-name { font-size: 34px; letter-spacing: 1.5px; }
  .card-back .brand-tagline { font-size: 10.5px; margin-top: 4px; letter-spacing: 2.2px; }
  .social { position: absolute; right: 24px; bottom: 10px; display: flex; gap: 3px; }
  .social span { width: 18px; height: 18px; border-radius: 50%; background: var(--white); display: block; }

  /* letterhead */
  .letterhead { left: 569px; top: 93px; width: 504px; height: 711px; }
  .letterhead .brand { left: 25px; top: 24px; color: var(--green); }
  .letterhead .brand-mark { width: 26px; height: 26px; }
  .letterhead .brand-name { font-size: 29px; }
  .letterhead .brand-tagline { font-size: 8px; color: var(--text-grey); margin-top: 3px; }
  .footer-band { position: absolute; left: 0; top: 662px; width: 504px; height: 42px; }
  .footer-text { position: absolute; left: 27px; color: var(--white); font-size: 8px; line-height: 1.25; display: flex; align-items: center; gap: 3px; white-space: nowrap; }
  .letterhead .web { color: var(--white); right: 32px; top: 687px; font-size: 9px; }
</style>
</head>
<body>

<section class="sheet card-front">
  <div class="brand">
    <div class="brand-row"><span class="brand-mark"></span><span class="brand-name">VORENTA</span></div>
    <span class="brand-tagline">PACKAGING TECHNOLOGY</span>
  </div>
  <svg class="name-band" viewBox="0 0 400 54">
    <polygon points="0,0 372,0 347,27 372,54 0,54" fill="var(--green)"/>
    <polygon points="384,0 400,0 400,54 384,54 359,27" fill="var(--grey)"/>
  </svg>
  <div class="holder">
    <div class="holder-name">Your Name</div>
    <div class="holder-role">Managing Director</div>
  </div>
  <div class="contact" style="top:157px">
    <svg width="7" height="10" viewBox="0 0 7 10"><rect x="0.5" y="0.5" width="6" height="9" rx="1" fill="var(--green)"/></svg>123 456 7890
    <svg width="10" height="8" viewBox="0 0 10 8" style="margin-left:4px"><rect x="0.5" y="0.5" width="9" height="7" fill="none" stroke="var(--green)"/><polyline points="0.5,0.5 5,4.5 9.5,0.5" fill="none" stroke="var(--green)"/></svg>name@vorenta.com
  </div>
  <div class="contact" style="top:174px; display:block">Your Office, Building, City<br>State XXXXX Country</div>
  <div class="contact" style="top:201px">
    <svg width="10" height="9" viewBox="0 0 10 9"><rect x="0.5" y="0.5" width="9" height="8" fill="none" stroke="var(--green)"/><rect x="2" y="2" width="2" height="5" fill="var(--green)"/></svg>123 456 7890
    <svg width="10" height="9" viewBox="0 0 10 9" style="margin-left:4px"><rect x="0.5" y="4" width="9" height="4.5" fill="none" stroke="var(--green)"/><rect x="2.5" y="0.5" width="5" height="3.5" fill="none" stroke="var(--green)"/></svg>123 456 7890
  </div>
  <div class="web">www.vorenta.com</div>
</section>

<section class="sheet card-back">
  <svg style="position:absolute;left:0;top:0" width="400" height="230" viewBox="0 0 400 230">
    <polygon points="222,0 400,0 400,230 227,230 107,114" fill="var(--green)"/>
  </svg>
  <div class="brand">
    <div class="brand-row"><span class="brand-mark"></span><span class="brand-name">VORENTA</span></div>
    <span class="brand-tagline">PACKAGING TECHNOLOGY</span>
  </div>
  <div class="social"><span></span><span></span><span></span></div>
</section>

<section class="sheet letterhead">
  <div class="brand">
    <div class="brand-row"><span class="brand-mark"></span><span class="brand-name">VORENTA</span></div>
    <span class="brand-tagline">PACKAGING TECHNOLOGY</span>
  </div>
  <svg class="footer-band" viewBox="0 0 504 42">
    <polygon points="0,0 482,0 465,21 482,42 0,42" fill="var(--green)"/>
    <polygon points="490,0 504,0 504,42 490,42 473,21" fill="var(--grey)"/>
  </svg>
  <div class="footer-text" style="top:666px; display:block">Your Office, Building, City<br>State XXXXX Country</div>
  <div class="footer-text" style="top:689px">
    <svg width="9" height="8" viewBox="0 0 9 8"><rect x="0.5" y="0.5" width="8" height="7" fill="none" stroke="var(--white)"/></svg>123 456 7890
    <svg width="9" height="8" viewBox="0 0 9 8" style="margin-left:3px"><rect x="0.5" y="3.5" width="8" height="4" fill="none" stroke="var(--white)"/><rect x="2" y="0.5" width="5" height="3" fill="none" stroke="var(--white)"/></svg>123 456 7890
  </div>
  <div class="web">www.vorenta.com</div>
</section>

</body>
</html>
```